The Molar Ledger (Cover Design for Ebook)

I need a cool and exciting eBook cover for my new book, launching very soon!
I want it to stand out and appeal to young professionals with big dreams.
It should be dramatic and bold and avoid cliche or generic photos. Simple design will work as long as it relates to the message of the book. The content will provide ten years of experience from working in the field and achieving success.
Title: The Molar Ledger (at the top)
(Subheading Updated) The secrets to money, motivation and success they don’t teach you in dental school
OR The secrets to success they don't teach you in dental school.
OR The secrets to money, motivation and success
(smaller under title)
Author Updated: Dr K Fenwick (place at the bottom)
Updates

Target Market(s)

Ambitious young dentists
See instagram www.snapverse.net/themolarledger for a sense of the style that I think could work.

Font styles to use
Serif
Sans Serif

Colors

Designer to choose colors to be used in the design.

Requirements
Must have
• Eye catching and cool.
• Show the benefits of success. Money, freedom, luxury
• Clear title and subheading
Nice to have
• Subtle dental reference
• dimensions 1600x2400
Should not have
• Boring photos of dentist/patients, dental clinic, teeth etc,

```html
<!DOCTYPE html>
<html lang="en">
<head>
<meta charset="utf-8">
<title>The Molar Ledger — Cover</title>
<link rel="stylesheet" href="https://fonts.googleapis.com/css2?family=Bebas+Neue&family=Roboto:ital,wght@1,400&display=swap">
<style>
  :root {
    --backdrop: #c4c5c4;
    --ink: #1c1b18;
    --cream: #fdf7cf;
    --sky-warm: #fcf3c4;
    --sky-cool: #8fd0cf;
    --sky-mid: #cfe8c9;
    --trophy-gold: #b58f48;
    --trophy-shadow: #5b4a6a;
  }
  * { box-sizing: border-box; margin: 0; padding: 0; }
  html, body { width: 1200px; height: 1200px; overflow: hidden; }
  body { background: var(--backdrop); position: relative; }

  .cover {
    position: absolute; left: 264px; top: 96px;
    width: 672px; height: 1008px;
    background: var(--cream);
    overflow: hidden;
  }
  .cover-photo {
    position: absolute; left: 0; top: 0; width: 672px; height: 930px;
    background:
      radial-gradient(ellipse 60% 50% at 10% 35%, var(--sky-warm) 0%, transparent 70%),
      linear-gradient(100deg, var(--sky-warm) 0%, var(--sky-mid) 55%, var(--sky-cool) 100%);
  }
  .trophy-photo {
    position: absolute; left: 150px; top: 408px; width: 460px; height: 522px;
    background:
      radial-gradient(ellipse 30% 42% at 48% 38%, rgba(181,143,72,0.85) 0%, rgba(181,143,72,0.35) 60%, transparent 100%),
      radial-gradient(ellipse 55% 30% at 50% 100%, rgba(91,74,106,0.55) 0%, transparent 100%);
  }

  .title-rules { position: absolute; left: 0; top: 0; }
  .title {
    position: absolute; left: 0; width: 100%;
    text-align: center; color: var(--ink);
    font-family: "Bebas Neue", "Oswald", sans-serif;
    line-height: 0.72;
  }
  .title-the { top: 44px; font-size: 74px; }
  .title-main { top: 108px; font-size: 143px; letter-spacing: 4px; }
  .title-sub { top: 224px; font-size: 120px; letter-spacing: 14px; padding-left: 14px; }

  .subtitle {
    position: absolute; left: 148px; width: 375px; top: 336px; height: 44px;
    border-top: 1px solid var(--ink); border-bottom: 1px solid var(--ink);
    display: flex; align-items: center; justify-content: center;
    font-family: "Roboto", sans-serif; font-style: italic;
    font-size: 17.5px; color: var(--ink); white-space: nowrap;
  }

  .author-rule {
    position: absolute; left: 0; top: 930px; width: 100%; height: 5px;
    background: var(--ink);
  }
  .author-band {
    position: absolute; left: 0; top: 935px; width: 100%; height: 73px;
    background: var(--cream);
    display: flex; align-items: center; justify-content: center;
  }
  .author {
    font-family: "Bebas Neue", "Oswald", sans-serif;
    font-size: 42px; letter-spacing: 23px; padding-left: 23px;
    color: var(--ink); line-height: 1;
  }
</style>
</head>
<body>
  <main class="cover">
    <div class="cover-photo"></div>
    <div class="trophy-photo" role="img" aria-label="Photo of two raised arms holding a gold trophy against a pale sky"></div>

    <svg class="title-rules" width="672" height="100" aria-hidden="true">
      <g stroke="#1c1b18" stroke-width="1.6">
        <line x1="104" y1="50" x2="279" y2="50"/>
        <line x1="104" y1="64" x2="279" y2="64"/>
        <line x1="104" y1="78" x2="279" y2="78"/>
        <line x1="388" y1="50" x2="563" y2="50"/>
        <line x1="388" y1="64" x2="563" y2="64"/>
        <line x1="388" y1="78" x2="563" y2="78"/>
      </g>
    </svg>

    <h1>
      <span class="title title-the">The</span>
      <span class="title title-main">Molar</span>
      <span class="title title-sub">Ledger</span>
    </h1>

    <p class="subtitle">The Secrets to Money, Motivation and Success</p>

    <div class="author-rule"></div>
    <div class="author-band"><p class="author">DR K FENWICK</p></div>
  </main>
</body>
</html>
```